Friendly and warm real estate investor business card

I'm looking for double-sided business cards to stick to the top of calendar magnets for a marketing campaign. They should include some type of statement(s) that I buy houses. ETA: See the project brief pdf for a photo of the calendar magnet -- look and feel of the business card should be similar / go with / coordinate.

The tone should be friendly and warm. I'm open to all options for colors. ETA: Although black can be one of the colors, it shouldn't be the primary color.

Contact information, magnet picture, and other specifications are in the attached design brief pdf.

Target Market(s)

Target audience is homeowners who would consider selling their house off-market. Target audience is non-owner occupied properties – properties with tenants, vacant properties, inherited properties, other real estate investors, etc.

Industry/Entity Type

Real Estate

Contact Information for Business Card

Name = Greta Halvorsen. Logo (Brindle Homes - see files attached). greta@brindlehomesgroup.com 703-482-3917 (call or text) 910-254-7130 (call or text) FB/IG: @brindlehomesgroup. QR code (see files attached). ETA: NO title/role should be included on the card.

Requirements
Must have
• Square corners. Horizontal orientation. Font shouldn’t be too small.
Nice to have
• Should include some type of statement or statements that I buy houses. Could include some of the benefits of selling a house off-market. Some potential phrases are included in the attached design brief pdf. Better suggestions are encouraged!!! Much “we buy houses” marketing is too cheesy and targeted to low-income areas. I am targeting sellers in a higher-cost of living area – but NOT “luxury” properties.

```html
<!DOCTYPE html>
<html lang="en">
<head>
<meta charset="utf-8">
<title>Brindle Homes – Greta Halvorsen</title>
<link rel="stylesheet" href="https://fonts.googleapis.com/css2?family=Comfortaa:wght@400;500&family=Allura&display=swap">
<style>
  :root {
    --sky-top: #3a2630;
    --sky-upper: #8a4343;
    --sky-mid: #c2594a;
    --sky-glow: #f47136;
    --sky-sun: #fbb43e;
    --sky-low: #d57a3a;
    --ground: #2e2a2a;
    --ink-light: #ffffff;
    --ink-dark: #111111;
    --band-edge: #eeae20;
    --band-core: #fde019;
  }
  * { box-sizing: border-box; margin: 0; padding: 0; }
  html, body {
    width: 1200px;
    height: 750px;
    overflow: hidden;
    background: #ffffff;
  }
  .card {
    position: relative;
    width: 1200px;
    height: 750px;
    overflow: hidden;
    font-family: "Comfortaa", sans-serif;
    color: var(--ink-light);
  }
  .card__backdrop {
    position: absolute;
    inset: 0;
    background:
      radial-gradient(ellipse 380px 120px at 600px 590px, rgba(255, 226, 110, 0.5), rgba(255, 226, 110, 0) 70%),
      linear-gradient(180deg,
        var(--sky-top) 0%,
        var(--sky-upper) 20%,
        var(--sky-mid) 36%,
        var(--sky-glow) 54%,
        var(--sky-sun) 74%,
        var(--sky-low) 84%,
        #6a4634 90%,
        var(--ground) 95%,
        var(--ground) 100%);
  }
  .card__frame {
    position: absolute;
    left: 0;
    top: 0;
    width: 1200px;
    height: 750px;
  }
  .brand {
    position: absolute;
    top: 98px;
    left: 0;
    width: 1200px;
    text-align: center;
    font-weight: 500;
    color: var(--ink-light);
    line-height: 1;
  }
  .brand__name {
    display: block;
    font-size: 66px;
    letter-spacing: 1px;
  }
  .brand__sub {
    display: block;
    margin-top: 2px;
    font-size: 25px;
    letter-spacing: 13px;
    padding-left: 13px;
  }
  .agent-name {
    position: absolute;
    top: 258px;
    left: 0;
    width: 1200px;
    text-align: center;
    font-family: "Allura", cursive;
    font-size: 150px;
    font-weight: 400;
    line-height: 1;
    color: var(--ink-light);
    white-space: nowrap;
    text-shadow: 1px 0 0 var(--ink-light), -1px 0 0 var(--ink-light);
  }
  .pitch {
    position: absolute;
    left: 159px;
    top: 449px;
    width: 890px;
    height: 121px;
    background: linear-gradient(90deg, var(--band-edge) 0%, #fcc21c 25%, var(--band-core) 50%, #fcc21c 75%, var(--band-edge) 100%);
    display: flex;
    flex-direction: column;
    justify-content: center;
    align-items: center;
    color: var(--ink-dark);
    font-weight: 500;
    font-size: 34px;
    letter-spacing: 2px;
    line-height: 1.2;
    text-transform: uppercase;
    white-space: nowrap;
  }
  .divider {
    position: absolute;
    left: 433px;
    top: 606px;
    width: 344px;
    height: 2px;
    background: var(--ink-light);
  }
  .contact__note {
    position: absolute;
    top: 640px;
    left: 0;
    width: 1200px;
    text-align: center;
    font-size: 32px;
    line-height: 1;
  }
  .contact__phones {
    position: absolute;
    top: 686px;
    left: 0;
    width: 1200px;
    display: flex;
    justify-content: center;
    align-items: center;
    gap: 28px;
    font-size: 33px;
    line-height: 1;
  }
  .contact__sep {
    width: 11px;
    height: 11px;
    border-radius: 50%;
    background: var(--ink-light);
  }
</style>
</head>
<body>
  <main class="card">
    <div class="card__backdrop" role="img" aria-label="Sunset sky in deep plum, orange and golden yellow over a silhouetted line of trees"></div>

    <svg class="card__frame" viewBox="0 0 1200 750" aria-hidden="true">
      <polyline points="341,710.5 37.5,710.5 37.5,39.5 1162.5,39.5 1162.5,710.5 866,710.5"
                fill="none" stroke="#ffffff" stroke-width="1.5"/>
    </svg>

    <header class="brand">
      <span class="brand__name">BRINDLE</span>
      <span class="brand__sub">HOMES</span>
    </header>

    <h1 class="agent-name">Greta Halvorsen</h1>

    <section class="pitch">
      <p>We're ready to buy your house today!</p>
      <p>Make your move and let us improve</p>
    </section>

    <div class="divider"></div>

    <p class="contact__note">(call or text)</p>
    <p class="contact__phones">
      <span>703-482-3917</span>
      <span class="contact__sep"></span>
      <span>910-254-7130</span>
    </p>
  </main>
</body>
</html>
```